Website redesign for fast growing company looking to present a unique image

We're looking to revamp our online image to represent the professional, accomplished company we have become. We want to move beyond a templated look and feel to a custom design - we are eager to have you design a new public face for us! In particular, we need creative ways to display text to stand out. We are reaching top-level, C-suite executives and want to give them the confidence that we have the skills, talent, expertise, and knowledge to help their companies grow.

Target Market(s)

contact centers, business process outsourcing

Industry/Entity Type

Call Center

Coding

Coded - Design and coding required

Number of Pages Required

4 page

Font styles to use
Sans Serif

Colors

Designer to choose colors to be used in the design.

Requirements
Must have
• Designed for a professional audience - C-suite executives - but that also shows our personality as a company that is nimble, personable, trustworthy, and smart. Must be lively, but not quirky. Professional, but not overly formal. Be bold with choices for imagery - we want to look unique so go beyond traditional "business/corporate" stock photos. Instead use imagery similar to what is on our staging website - korvanta.com/staging. Do not use the "neon" sign. Use colors to match and complement our logo - bright orange and dark blue. Creative text boxes that we can use throughout the site. I have attached pages of our current staging site to display some of the types of imagery that might work. We are looking for "professional with a personality" Note: this design will be transferred into a Wordpress framework.
Nice to have
• We like the animated text features of the Tellbrook.com site - bold colors, great display of text features that break up the page and engage people to continue scrolling.
Should not have
• Cheesy stock photos of call center agents wearing headsets. Overly used stock photos of professionals in suits shaking hands, high-rise buildings, connection/network graphics. Current management does not like the neon sign graphics displayed on our staging site (korvanta.com/staging). We do not like style of sites that use cartoon-like icons and figures.

```html
<!DOCTYPE html>
<html lang="en">
<head>
<meta charset="utf-8">
<title>Korvanta – Home and Leadership Pages</title>
<link href="https://fonts.googleapis.com/css2?family=Arimo:wght@400;700&display=swap" rel="stylesheet">
<style>
:root{
  --navy:#2a4a6e;
  --orange:#e35a26;
  --white:#ffffff;
  --ink:#1d1d1d;
  --mist:#c7d4e1;
  --ring:#c9c9c9;
}
*{box-sizing:border-box;margin:0;padding:0}
html,body{width:857px;height:1200px;overflow:hidden;background:var(--white)}
body{font-family:"Arimo",Arial,sans-serif;color:var(--ink)}
.stage{position:absolute;left:0;top:0;width:1624px;height:2274px;transform:scale(0.52771);transform-origin:0 0}
.page{position:absolute;top:0;overflow:hidden;background:var(--white)}
.page--home{left:40px;width:758px;height:2274px}
.page--team{left:822px;width:765px;height:1593px}
.abs{position:absolute}
.shapes{position:absolute;left:0;top:0}

/* header */
.brand{position:absolute;font-size:36px;font-weight:400;color:var(--orange);letter-spacing:-0.5px}
.nav{position:absolute;display:flex;gap:11px;font-size:10px;color:var(--white);white-space:nowrap}
.nav a{color:inherit;text-decoration:none;padding-bottom:5px}
.nav a.is-active{border-bottom:2px solid var(--orange)}
.search{position:absolute;width:113px;height:14px;background:var(--white);border-radius:3px}
.search svg{position:absolute;right:4px;top:2px}

/* type */
.h-display{font-size:31px;line-height:38px;font-weight:400;color:var(--white)}
.h-display--orange{color:var(--orange)}
.h-section{font-size:31px;font-weight:700;color:var(--orange);text-align:center}
.copy{font-size:15px;line-height:23px;color:var(--white)}
.copy p+p{margin-top:22px}
.copy--dark{color:var(--ink)}
.btn{position:absolute;background:var(--white);color:var(--ink);font-size:15px;display:flex;align-items:center;justify-content:center;letter-spacing:0.3px}
.fine{font-size:11px;line-height:19px;color:var(--white)}

/* value circles */
.value{position:absolute;width:152px;height:152px;border-radius:50%;display:flex;align-items:center;justify-content:center;text-align:center;color:var(--white);font-size:15px;line-height:23px}

/* process labels */
.step{position:absolute;width:110px;text-align:center;font-size:15px;color:#4f5660}
.step--data{color:var(--white)}

/* footer */
.footer{position:absolute;left:0;background:var(--navy)}
.social{position:absolute;display:flex;gap:7px}
.social span{width:17px;height:17px;border:2px solid var(--white);border-radius:50%}

/* team */
.member{position:absolute;width:150px}
.member .photo{width:120px;height:126px}
.member .name{margin-top:12px;font-size:11px;color:var(--ink)}
.member .role{font-size:8px;color:var(--ink);margin-top:2px}
.member .links{display:flex;gap:6px;margin-top:12px;align-items:center}
.member .links .profile{width:16px;height:16px;border:1.5px solid var(--ink)}
</style>
</head>
<body>
<div class="stage">

  <!-- HOME PAGE -->
  <section class="page page--home">
    <svg class="shapes" width="758" height="2274" viewBox="0 0 758 2274">
      <defs>
        <linearGradient id="gHero" x1="0" y1="0" x2="1" y2="1">
          <stop offset="0" stop-color="#b9b3a8"/><stop offset=".5" stop-color="#c88a62"/><stop offset="1" stop-color="#6d5a4c"/>
        </linearGradient>
        <linearGradient id="gCta" x1="0" y1="0" x2="1" y2="1">
          <stop offset="0" stop-color="#a98a6c"/><stop offset=".6" stop-color="#5b3f2e"/><stop offset="1" stop-color="#c7b7a2"/>
        </linearGradient>
        <clipPath id="heroClip"><circle cx="222" cy="333" r="218"/></clipPath>
        <marker id="arrow" viewBox="0 0 10 10" refX="8" refY="5" markerWidth="7" markerHeight="7" orient="auto">
          <path d="M0 1 L9 5 L0 9" fill="none" stroke="#e35a26" stroke-width="1.6"/>
        </marker>
      </defs>
      <rect x="0" y="0" width="758" height="868" fill="var(--navy)"/>
      <circle cx="222" cy="333" r="233" fill="var(--orange)"/>
      <rect x="0" y="378" width="758" height="490" fill="var(--orange)"/>
      <circle cx="700" cy="470" r="215" fill="var(--navy)"/>
      <g clip-path="url(#heroClip)">
        <rect x="0" y="100" width="460" height="278" fill="url(#gHero)" role="img" aria-label="Photo of a team joining hands in a high five"/>
      </g>
      <rect x="545" y="418" width="143" height="96" rx="10" fill="#ffffff" opacity=".9"/>

      <g fill="var(--navy)" stroke="var(--navy)">
        <circle cx="130" cy="1088" r="82" fill="none" stroke-width="2"/>
        <circle cx="292" cy="1088" r="82" fill="none" stroke-width="2"/>
        <circle cx="458" cy="1088" r="82" fill="none" stroke-width="2"/>
        <circle cx="620" cy="1088" r="82" fill="none" stroke-width="2"/>
      </g>

      <g fill="var(--mist)" stroke="#8e97a2" stroke-width="2">
        <circle cx="120" cy="1541" r="55"/>
        <circle cx="248" cy="1541" r="55"/>
        <circle cx="374" cy="1541" r="55"/>
        <circle cx="500" cy="1541" r="55"/>
      </g>
      <circle cx="627" cy="1541" r="70" fill="var(--ring)"/>
      <circle cx="627" cy="1541" r="53" fill="var(--orange)"/>
      <g fill="none" stroke="var(--orange)" stroke-width="1.5" marker-end="url(#arrow)">
        <path d="M250 1486 C 250 1410, 360 1410, 360 1488"/>
        <path d="M510 1486 C 510 1410, 617 1410, 617 1472"/>
        <path d="M122 1597 C 122 1672, 235 1672, 235 1598"/>
        <path d="M387 1597 C 387 1672, 500 1672, 500 1598"/>
      </g>

      <rect x="0" y="1731" width="375" height="342" fill="var(--orange)"/>
      <rect x="375" y="1731" width="383" height="342" fill="url(#gCta)" role="img" aria-label="Photo of two women studying notes together at a table"/>
    </svg>

    <div class="brand" style="left:60px;top:30px">Korvanta</div>
    <nav class="nav" style="left:268px;top:49px">
      <a class="is-active">Home</a><a>Markets We Serve</a><a>About Us</a><a>Contact</a><a>Apply Today</a>
    </nav>
    <div class="search" style="left:580px;top:48px">
      <svg width="10" height="10" viewBox="0 0 10 10"><circle cx="4" cy="4" r="3" fill="none" stroke="#e35a26" stroke-width="1.4"/><path d="M6 6 L9 9" stroke="#e35a26" stroke-width="1.6"/></svg>
    </div>

    <h1 class="abs h-display h-display--orange" style="left:463px;top:138px">We Are Korvanta.</h1>
    <p class="abs copy" style="left:463px;top:186px;width:240px">Personalized Customer Service, Tech Support, and Business Services at Scale.</p>
    <a class="btn" style="left:466px;top:340px;width:226px;height:35px">HOW CAN WE HELP YOU?</a>
    <p class="abs fine" style="left:517px;top:530px;width:200px;text-align:center">#28 on the 2017 APEX 500<br>listed in 2018 and 2019</p>

    <h2 class="abs h-display" style="left:60px;top:412px;width:400px">Nimble. Agile. Responsive. Focused.</h2>
    <div class="abs copy" style="left:62px;top:503px;width:390px">
      <p>Korvanta delivers personalized customer service, tech support, and business services at scale to your customers, members, employees, and citizens. We are a true partner and work by your side to help you achieve your goals.</p>
      <p>100% US based with 100% US employees, we serve State and Federal Government Agencies and Commercial businesses with a full suite of outsourcing solutions.</p>
      <p>If you're ready to streamline operations, improve your top and bottom line, and bring more professionalism and performance to your customer interactions, we can help.</p>
    </div>

    <h2 class="abs h-section" style="left:0;top:918px;width:710px">Our Core Values</h2>
    <p class="abs" style="left:0;top:956px;width:710px;text-align:center;font-size:15px">These guide every member of our team, every day.</p>
    <div class="value" style="left:54px;top:1012px;background:var(--navy)">Make Every<br>Interaction<br>Count</div>
    <div class="value" style="left:216px;top:1012px;background:var(--navy)">Act With<br>Respect and<br>Integrity</div>
    <div class="value" style="left:382px;top:1012px;background:var(--navy)">Demonstrate<br>Passion for<br>Continuous<br>Improvement</div>
    <div class="value" style="left:544px;top:1012px;background:var(--navy)">Be Worthy of<br>Trust From All<br>Stakeholders</div>

    <h2 class="abs h-section" style="left:0;top:1243px;width:748px">Our Proven Process</h2>
    <p class="abs copy copy--dark" style="left:70px;top:1302px;width:608px;text-align:center">Dedicated teams that deliver personalized service at scale + Highly engaged agents with critical thinking skills + A proprietary analytics platform to help you make data-driven decisions + Customized services to meet your KPIs&nbsp; + Cloud-based technologies for fast onboarding and flexible staffing</p>
    <div class="step" style="left:65px;top:1532px">INSIGHT</div>
    <div class="step" style="left:193px;top:1532px">TEAM</div>
    <div class="step" style="left:319px;top:1532px">PASSION</div>
    <div class="step" style="left:445px;top:1532px">CURIOSITY</div>
    <div class="step step--data" style="left:572px;top:1532px">DATA</div>

    <h2 class="abs h-display" style="left:60px;top:1770px;font-weight:700">Take Charge of<br>Your Future</h2>
    <p class="abs copy" style="left:60px;top:1863px;width:285px">Take the first step to get your business on a better track. Schedule a call so we can learn more about each other and find the right path forward.</p>
    <a class="btn" style="left:59px;top:1996px;width:188px;height:35px">GET STARTED</a>

    <footer class="footer" style="top:2073px;width:758px;height:201px">
      <p class="abs fine" style="left:69px;top:32px">Copyright 2020 Korvanta</p>
      <div class="social" style="left:67px;top:67px"><span></span><span></span><span></span><span></span></div>
      <p class="abs fine" style="left:503px;top:31px;line-height:23px">Korvanta is Powered with 100%<br>Green Energy</p>
      <div class="abs" style="left:504px;top:84px;width:122px;height:54px;background:var(--white);border:3px solid #1d4f9c"></div>
    </footer>
  </section>

  <!-- LEADERSHIP PAGE -->
  <section class="page page--team">
    <svg class="shapes" width="765" height="1593" viewBox="0 0 765 1593">
      <defs>
        <linearGradient id="gMeet" x1="0" y1="0" x2="1" y2="1">
          <stop offset="0" stop-color="#b08e6a"/><stop offset=".5" stop-color="#d9cdbd"/><stop offset="1" stop-color="#8d6f58"/>
        </linearGradient>
        <clipPath id="meetClip"><circle cx="665" cy="190" r="215"/></clipPath>
      </defs>
      <rect x="0" y="0" width="765" height="90" fill="var(--navy)"/>
      <rect x="0" y="90" width="765" height="376" fill="var(--orange)"/>
      <g clip-path="url(#meetClip)">
        <rect x="440" y="90" width="325" height="320" fill="url(#gMeet)" role="img" aria-label="Photo of colleagues greeting each other around a meeting table"/>
      </g>
    </svg>

    <div class="brand" style="left:62px;top:20px">Korvanta</div>
    <nav class="nav" style="left:272px;top:38px">
      <a>Home</a><a>Markets We Serve</a><a class="is-active">About Us</a><a>Contact</a><a>Apply Today</a>
    </nav>
    <div class="search" style="left:585px;top:37px">
      <svg width="10" height="10" viewBox="0 0 10 10"><circle cx="4" cy="4" r="3" fill="none" stroke="#e35a26" stroke-width="1.4"/><path d="M6 6 L9 9" stroke="#e35a26" stroke-width="1.6"/></svg>
    </div>

    <h1 class="abs h-display" style="left:64px;top:184px">Korvanta<br>Leadership Team</h1>
    <p class="abs copy" style="left:66px;top:275px;width:345px">Let us help you build the business you want with better people, streamlined operations, improved client experiences, and stronger results.</p>

    <h2 class="abs h-section" style="left:0;top:550px;width:720px">Meet Our Team</h2>

    <div class="member" style="left:88px;top:613px"><div class="photo" style="background:linear-gradient(160deg,#e7e3dc,#c9a77f)" role="img" aria-label="Portrait of Marlene T. Okafor"></div><p class="name">Marlene T. Okafor</p><p class="role">Founder &amp; CEO</p><div class="links"><span class="profile"></span><svg width="22" height="16" viewBox="0 0 22 16"><rect x="1" y="1" width="20" height="14" fill="none" stroke="#1d1d1d" stroke-width="1.4"/><path d="M1 1 L11 9 L21 1 M1 15 L8 7 M21 15 L14 7" fill="none" stroke="#1d1d1d" stroke-width="1.2"/></svg></div></div>
    <div class="member" style="left:250px;top:613px"><div class="photo" style="background:linear-gradient(160deg,#8a8582,#d7c19e)" role="img" aria-label="Portrait of Dana Whitcombe"></div><p class="name">Dana Whitcombe</p><p class="role">CFO</p><div class="links"><span class="profile"></span><svg width="22" height="16" viewBox="0 0 22 16"><rect x="1" y="1" width="20" height="14" fill="none" stroke="#1d1d1d" stroke-width="1.4"/><path d="M1 1 L11 9 L21 1 M1 15 L8 7 M21 15 L14 7" fill="none" stroke="#1d1d1d" stroke-width="1.2"/></svg></div></div>
    <div class="member" style="left:408px;top:613px"><div class="photo" style="background:linear-gradient(160deg,#7b7b7b,#cfc0ad 55%,#3b3b3b)" role="img" aria-label="Portrait of Victor Almanza"></div><p class="name">Victor Almanza</p><p class="role">CIO</p><div class="links"><span class="profile"></span><svg width="22" height="16" viewBox="0 0 22 16"><rect x="1" y="1" width="20" height="14" fill="none" stroke="#1d1d1d" stroke-width="1.4"/><path d="M1 1 L11 9 L21 1 M1 15 L8 7 M21 15 L14 7" fill="none" stroke="#1d1d1d" stroke-width="1.2"/></svg></div></div>
    <div class="member" style="left:564px;top:613px"><div class="photo" style="background:linear-gradient(160deg,#d9b58e,#c99b7c 55%,#24262b)" role="img" aria-label="Portrait of Gordon Pell"></div><p class="name">Gordon Pell</p><p class="role">VP Operations</p><div class="links"><span class="profile"></span><svg width="22" height="16" viewBox="0 0 22 16"><rect x="1" y="1" width="20" height="14" fill="none" stroke="#1d1d1d" stroke-width="1.4"/><path d="M1 1 L11 9 L21 1 M1 15 L8 7 M21 15 L14 7" fill="none" stroke="#1d1d1d" stroke-width="1.2"/></svg></div></div>

    <div class="member" style="left:90px;top:850px"><div class="photo" style="background:linear-gradient(160deg,#cfcac2,#d4a98f 55%,#2d3040)" role="img" aria-label="Portrait of Stuart Lindqvist"></div><p class="name">Stuart Lindqvist</p><p class="role">VP Human Resources</p><div class="links"><span class="profile"></span><svg width="22" height="16" viewBox="0 0 22 16"><rect x="1" y="1" width="20" height="14" fill="none" stroke="#1d1d1d" stroke-width="1.4"/><path d="M1 1 L11 9 L21 1 M1 15 L8 7 M21 15 L14 7" fill="none" stroke="#1d1d1d" stroke-width="1.2"/></svg></div></div>
    <div class="member" style="left:250px;top:850px"><div class="photo" style="background:linear-gradient(160deg,#8e8a82,#c9a184 55%,#d8dde6)" role="img" aria-label="Portrait of Neil Brantford"></div><p class="name">Neil Brantford</p><p class="role">VP Information Technology</p><div class="links"><span class="profile"></span><svg width="22" height="16" viewBox="0 0 22 16"><rect x="1" y="1" width="20" height="14" fill="none" stroke="#1d1d1d" stroke-width="1.4"/><path d="M1 1 L11 9 L21 1 M1 15 L8 7 M21 15 L14 7" fill="none" stroke="#1d1d1d" stroke-width="1.2"/></svg></div></div>
    <div class="member" style="left:408px;top:850px"><div class="photo" style="background:linear-gradient(160deg,#2d4a7a,#d8c3ad 55%,#1f2a44)" role="img" aria-label="Portrait of Joanne Mercer"></div><p class="name">Joanne Mercer</p><p class="role">Director of Business Development</p><div class="links"><span class="profile"></span><svg width="22" height="16" viewBox="0 0 22 16"><rect x="1" y="1" width="20" height="14" fill="none" stroke="#1d1d1d" stroke-width="1.4"/><path d="M1 1 L11 9 L21 1 M1 15 L8 7 M21 15 L14 7" fill="none" stroke="#1d1d1d" stroke-width="1.2"/></svg></div></div>
    <div class="member" style="left:564px;top:850px"><div class="photo" style="background:linear-gradient(160deg,#c7ccd2,#d6b09a 55%,#8aa3c8)" role="img" aria-label="Portrait of Warren Tidwell"></div><p class="name">Warren Tidwell</p><p class="role">Director of Information Technology</p><div class="links"><span class="profile"></span><svg width="22" height="16" viewBox="0 0 22 16"><rect x="1" y="1" width="20" height="14" fill="none" stroke="#1d1d1d" stroke-width="1.4"/><path d="M1 1 L11 9 L21 1 M1 15 L8 7 M21 15 L14 7" fill="none" stroke="#1d1d1d" stroke-width="1.2"/></svg></div></div>

    <div class="member" style="left:88px;top:1096px"><div class="photo" style="background:linear-gradient(160deg,#d3d3d3,#e0b496 55%,#a9c8c2)" role="img" aria-label="Portrait of Leah Castellano"></div><p class="name">Leah Castellano</p><p class="role">Director of Human Resources</p><div class="links"><span class="profile"></span><svg width="22" height="16" viewBox="0 0 22 16"><rect x="1" y="1" width="20" height="14" fill="none" stroke="#1d1d1d" stroke-width="1.4"/><path d="M1 1 L11 9 L21 1 M1 15 L8 7 M21 15 L14 7" fill="none" stroke="#1d1d1d" stroke-width="1.2"/></svg></div></div>
    <div class="member" style="left:248px;top:1096px"><div class="photo" style="background:linear-gradient(160deg,#d8d8d8,#c99a80 55%,#4a5264)" role="img" aria-label="Portrait of Martin Rusk"></div><p class="name">Martin Rusk</p><p class="role">Controller</p><div class="links"><span class="profile"></span><svg width="22" height="16" viewBox="0 0 22 16"><rect x="1" y="1" width="20" height="14" fill="none" stroke="#1d1d1d" stroke-width="1.4"/><path d="M1 1 L11 9 L21 1 M1 15 L8 7 M21 15 L14 7" fill="none" stroke="#1d1d1d" stroke-width="1.2"/></svg></div></div>
    <div class="member" style="left:410px;top:1096px"><div class="photo" style="background:linear-gradient(160deg,#cfcfcf,#6b4a34 45%,#2a2f48)" role="img" aria-label="Portrait of Bree Hollander"></div><p class="name">Bree Hollander</p><p class="role">Sites Manager</p><div class="links"><span class="profile"></span><svg width="22" height="16" viewBox="0 0 22 16"><rect x="1" y="1" width="20" height="14" fill="none" stroke="#1d1d1d" stroke-width="1.4"/><path d="M1 1 L11 9 L21 1 M1 15 L8 7 M21 15 L14 7" fill="none" stroke="#1d1d1d" stroke-width="1.2"/></svg></div></div>

    <footer class="footer" style="top:1392px;width:765px;height:201px">
      <p class="abs fine" style="left:70px;top:33px">Copyright 2020 Korvanta</p>
      <div class="social" style="left:68px;top:67px"><span></span><span></span><span></span><span></span></div>
      <p class="abs fine" style="left:507px;top:32px;line-height:23px">Korvanta is Powered with 100%<br>Green Energy</p>
      <div class="abs" style="left:508px;top:85px;width:124px;height:54px;background:var(--white);border:3px solid #1d4f9c"></div>
    </footer>
  </section>

</div>
</body>
</html>
```